Vegan Jerky company needs a label for it's pouch, and a new logo

Dear Designers - this used to be a guaranteed project, however, due to the low quality of designs I have received, I have removed the guaranteed status. However, we need this product made and we will pay for a great, high quality design that meets the requirements of our brief.

We need sticker labels that will go onto the front and back of our vegan jerky package. Our package is a zip-sealable pouch, and we will either go with black, white or brown for the color of the pouch.

We need the concept, artwork, theme and logo designed. Pls choose the colors.

There will be four flavors. These can be finished as part of another project. The flavors are: Smoked Maple, Cracked Pepper, Teriyaki Sriracha, Original.

We are Lonny and Perla's Vegan Jerky.

Our food is vegan, non GMO, straight from the farm, organic, healthy, pure, clean, made in small batches and earth friendly. We use no chemicals or artificial flavors and our product is 100% natural.

Our kitchen is yours.

Target Market(s)

Vegetarians, vegans, health conscious, ecological, intelligent, caring.

Industry/Entity Type

Food Production

Logo Text

"Lonny and Perla" and "Our Kitchen is Yours"

Colors

Designer to choose colors to be used in the design.

Requirements
Must have
• earth friendly design, classy, hipster, vegan design, shabby chic,
Nice to have
• i have no ideas really...
• We prefer black and while, with a little splash of color. The last file is an idea I had but please use your own vision.

```html
<!DOCTYPE html>
<html lang="en">
<head>
<meta charset="utf-8">
<title>Lonny &amp; Perla's Vegan Jerky – Smoked Maple Label</title>
<link rel="stylesheet" href="https://fonts.googleapis.com/css2?family=Oswald:wght@500;700&family=Josefin+Sans:wght@400;600&display=swap">
<style>
  :root {
    --backdrop: #e4e4e4;
    --label-white: #f1f1f1;
    --paper: #e9e9e9;
    --jerky-red: #8e2424;
    --ribbon-red: #b34a4a;
    --ink: #2e2e2e;
    --ink-soft: #555555;
    --pattern-grey: #b9b9b9;
    --rule-blue: #6f7889;
    --illustration-tone: #8a8a8a;
  }
  * { box-sizing: border-box; margin: 0; padding: 0; }
  html, body { width: 1200px; height: 1200px; overflow: hidden; background: var(--backdrop); }
  .canvas { position: relative; width: 1200px; height: 1200px; overflow: hidden; }

  .pouch-label {
    position: absolute; left: 304px; top: 96px; width: 616px; height: 992px;
    background: var(--paper);
  }
  .side-band { position: absolute; top: 0; bottom: 0; width: 60px; background: var(--jerky-red); }
  .side-band--left { left: 0; }
  .side-band--right { right: 0; width: 50px; }

  .pattern-band {
    position: absolute; left: 60px; right: 50px; background: var(--pattern-grey);
    opacity: .75;
  }
  .pattern-band--top { top: 14px; height: 60px; }
  .pattern-band--bottom { bottom: 14px; height: 52px; }

  .inner-frame {
    position: absolute; left: 68px; right: 58px; top: 84px; bottom: 78px;
    border: 10px solid var(--ribbon-red); outline: 1px solid var(--jerky-red); outline-offset: -14px;
    background: var(--label-white);
  }

  .illustration { position: absolute; background: linear-gradient(180deg, #a9a9a9, var(--illustration-tone)); border-radius: 6px; opacity: .8; }
  .illustration--cook { left: 104px; top: 204px; width: 130px; height: 98px; }
  .illustration--guest { left: 366px; top: 196px; width: 124px; height: 110px; }

  .brand-mark {
    position: absolute; left: 236px; top: 214px; width: 130px; text-align: center;
    font-family: "Oswald", sans-serif; font-weight: 700; font-size: 44px; line-height: 1.2; color: var(--ribbon-red);
  }

  .name-band {
    position: absolute; left: 0; right: 0; top: 318px; height: 200px; background: #f7f7f7;
    border-top: 3px double var(--rule-blue); border-bottom: 3px double var(--rule-blue);
  }
  .ribbon {
    position: absolute; left: 146px; top: 306px; width: 340px; height: 66px;
    background: var(--ribbon-red);
    clip-path: polygon(0 0, 100% 0, 94% 50%, 100% 100%, 0 100%, 6% 50%);
    display: flex; align-items: center; justify-content: center;
    font-family: "Oswald", sans-serif; font-weight: 700; font-size: 40px; color: #fff; letter-spacing: .5px;
    white-space: nowrap;
  }
  .product-title {
    position: absolute; left: 36px; top: 380px; white-space: nowrap;
    font-family: "Oswald", sans-serif; font-weight: 700; font-size: 86px; line-height: 1.1;
    color: var(--ink); letter-spacing: 0;
  }
  .established {
    position: absolute; left: 526px; top: 418px; white-space: nowrap;
    font-family: "Oswald", sans-serif; font-weight: 700; font-size: 30px; line-height: 1.1; color: var(--jerky-red);
  }
  .established span { display: block; border-bottom: 3px solid var(--jerky-red); margin-bottom: 2px; }

  .flavour-box {
    position: absolute; left: 132px; top: 572px; width: 378px; height: 142px;
    border: 4px solid var(--ink); border-top: none;
  }
  .flavour-box::before, .flavour-box::after {
    content: ""; position: absolute; top: 0; height: 4px; width: 88px; background: var(--ink);
  }
  .flavour-box::before { left: 0; }
  .flavour-box::after { right: 0; }
  .flavour-kicker {
    position: absolute; left: 0; right: 0; top: -15px; text-align: center; line-height: 30px;
    font-family: "Josefin Sans", sans-serif; font-weight: 400; font-size: 26px; letter-spacing: 7px; color: var(--ink);
  }
  .flavour-name {
    position: absolute; left: -50px; right: -50px; top: 18px; text-align: center; white-space: nowrap;
    font-family: "Oswald", sans-serif; font-weight: 700; font-size: 64px; line-height: 1.1; color: var(--ink);
  }
  .tagline {
    position: absolute; left: 0; right: 0; top: 102px; text-align: center; white-space: nowrap;
    font-family: "Josefin Sans", sans-serif; font-weight: 400; font-size: 22px; line-height: 26px; color: var(--jerky-red);
  }

  .info-row { position: absolute; left: 108px; top: 746px; width: 420px; height: 150px; }
  .info-row svg { position: absolute; inset: 0; }
  .info-text {
    position: absolute; left: 20px; width: 90px; text-align: center;
    font-family: "Oswald", sans-serif; font-weight: 500; font-size: 20px; line-height: 1.2; color: var(--ink);
  }
  .info-text--purity { top: 28px; }
  .info-text--weight { top: 100px; }
  .tree-art { position: absolute; left: 176px; top: 18px; width: 104px; height: 114px; border-radius: 6px;
    background: linear-gradient(180deg, #5a5a5a, #8c8c8c); opacity: .85; }
</style>
</head>
<body>
<main class="canvas">
  <section class="pouch-label" aria-label="Lonny &amp; Perla's Vegan Jerky, Smoked Maple front label">
    <div class="side-band side-band--left"></div>
    <div class="side-band side-band--right"></div>
    <div class="pattern-band pattern-band--top" role="img" aria-label="Grey key-pattern border"></div>
    <div class="inner-frame"></div>
    <div class="pattern-band pattern-band--bottom" role="img" aria-label="Grey key-pattern border"></div>

    <div class="illustration illustration--cook" role="img" aria-label="Vintage engraving of a cook serving a dish"></div>
    <div class="illustration illustration--guest" role="img" aria-label="Vintage engraving of a hatted guest at a tea table"></div>
    <div class="brand-mark">L&amp;P</div>

    <div class="name-band"></div>
    <div class="ribbon">LONNY &amp; PERLA'S</div>
    <h1 class="product-title">VEGAN JERKY</h1>
    <div class="established"><span>EST.</span>2017</div>

    <div class="flavour-box">
      <p class="flavour-kicker">ORIGINAL</p>
      <h2 class="flavour-name">SMOKED MAPLE</h2>
      <p class="tagline">« OUR KITCHEN IS YOURS »</p>
    </div>

    <div class="info-row">
      <svg width="420" height="150" viewBox="0 0 420 150" aria-hidden="true">
        <g stroke="#555" stroke-width="1.5" fill="none">
          <line x1="10" y1="4" x2="410" y2="4" stroke-dasharray="4 4"/>
          <line x1="10" y1="142" x2="410" y2="142" stroke-dasharray="4 4"/>
          <polyline points="16,0 10,4 16,8"/>
          <polyline points="404,0 410,4 404,8"/>
          <polyline points="16,138 10,142 16,146"/>
          <polyline points="404,138 410,142 404,146"/>
          <line x1="130" y1="22" x2="130" y2="130" stroke-dasharray="2 4"/>
          <line x1="326" y1="22" x2="326" y2="130" stroke-dasharray="2 4"/>
          <line x1="36" y1="88" x2="96" y2="88" stroke-dasharray="2 2"/>
        </g>
        <circle cx="368" cy="46" r="20" fill="#3a3a3a"/>
        <circle cx="368" cy="104" r="20" fill="#3a3a3a"/>
      </svg>
      <p class="info-text info-text--purity">100%<br>PURE</p>
      <p class="info-text info-text--weight">500 GM</p>
      <div class="tree-art" role="img" aria-label="Silhouette of a maple tree"></div>
    </div>
  </section>
</main>
</body>
</html>
```